Silver Bloom Marisol's Cleaning Service Business Cards Project

A business card with all contact details with logo design on there (already have a logo) eye catching Logo and contact info on one side, full logo on the back, must target upper class residential and corporate companies, fitness companies, still keep it on the feminine side of things , must look elegant

Target Market(s)

Upper class homes and corporate companies

Industry/Entity Type

Cleaning Service

Contact Information for Business Card

Name: Marisol Venturo
Position: Director
ABN: 47193802564
Email: marisolssilvercleaning@fernmail.test
Number: 0417968341

Font styles to use
Decorative

Colors

Designer to choose colors to be used in the design.

Requirements
Must have
• Available Sydney Wide, contact info and logo on one side, full logo on the back
Nice to have
• Professional appearance
Should not have
• Cheap advert looking stuff

```html
<!DOCTYPE html>
<html lang="en">
<head>
<meta charset="utf-8">
<title>Silver Bloom Marisol's Cleaning Service — Business Cards</title>
<link rel="stylesheet" href="https://fonts.googleapis.com/css2?family=Noto+Serif:wght@700&family=Roboto:wght@400;500&display=swap">
<style>
  :root {
    --backdrop: #2c2c2e;
    --slate: #3a4350;
    --slate-deep: #2f3742;
    --teal: #6cc5c8;
    --ink: #3b3b3b;
    --rule: #b9b9b9;
    --paper: #ffffff;
  }
  * { box-sizing: border-box; margin: 0; padding: 0; }
  html, body {
    width: 1200px; height: 900px; overflow: hidden;
    background: var(--backdrop);
  }
  .canvas { position: relative; width: 1200px; height: 900px; }

  .card {
    position: absolute;
    width: 600px; height: 340px;
    box-shadow: 0 10px 24px rgba(0,0,0,.45);
  }

  /* Front: brand side */
  .card-front {
    left: 380px; top: 80px;
    background: linear-gradient(160deg, var(--slate-deep), var(--slate) 70%);
    display: flex; flex-direction: column; align-items: center; justify-content: center;
    color: var(--teal);
    font-family: "Noto Serif", Georgia, serif;
    font-weight: 700;
  }
  .brand-dot {
    width: 56px; height: 56px; border-radius: 50%;
    background: var(--teal);
    margin-bottom: 26px;
  }
  .brand-name {
    font-size: 38px; letter-spacing: 2px; text-transform: uppercase; line-height: 1;
  }
  .brand-tagline {
    margin-top: 12px;
    font-size: 12px; letter-spacing: 5px; text-transform: uppercase;
  }

  /* Back: contact side */
  .card-back {
    left: 240px; top: 480px;
    background: var(--paper);
    font-family: "Roboto", Arial, sans-serif;
    color: var(--ink);
    text-align: center;
    padding-top: 62px;
  }
  .contact-name {
    font-family: "Noto Serif", Georgia, serif;
    font-weight: 700; font-size: 34px; color: var(--teal); letter-spacing: .5px;
    line-height: 1;
  }
  .contact-role { margin-top: 6px; font-size: 19px; }
  .divider {
    width: 52px; height: 2px; background: var(--rule);
    margin: 22px auto 22px;
  }
  .contact-line {
    display: flex; align-items: center; justify-content: center; gap: 8px;
    font-size: 21px; line-height: 1.3;
  }
  .contact-line svg { flex: none; }
  .contact-abn { margin-top: 10px; }
  .abn-label { color: var(--teal); font-weight: 500; }
  .accent-band {
    position: absolute; left: 0; right: 0; bottom: 0; height: 10px;
    background: var(--teal);
  }
</style>
</head>
<body>
<main class="canvas">

  <section class="card card-front" aria-label="Business card front">
    <div class="brand-dot"></div>
    <div class="brand-name">Silver Bloom</div>
    <div class="brand-tagline">Marisol's Cleaning Service</div>
  </section>

  <section class="card card-back" aria-label="Business card back">
    <h1 class="contact-name">Marisol Venturo</h1>
    <p class="contact-role">Director</p>
    <div class="divider"></div>
    <p class="contact-line">
      <svg width="16" height="18" viewBox="0 0 24 24" aria-hidden="true">
        <path fill="#6cc5c8" d="M6.6 10.8c1.4 2.8 3.8 5.1 6.6 6.6l2.2-2.2c.3-.3.7-.4 1-.2 1.1.4 2.3.6 3.6.6.6 0 1 .4 1 1V20c0 .6-.4 1-1 1C10.6 21 3 13.4 3 4c0-.6.4-1 1-1h3.5c.6 0 1 .4 1 1 0 1.3.2 2.5.6 3.6.1.3 0 .7-.2 1z"/>
      </svg>
      0417968341
    </p>
    <p class="contact-line">
      <svg width="22" height="16" viewBox="0 0 22 16" aria-hidden="true">
        <rect x="1" y="1" width="20" height="14" fill="none" stroke="#6cc5c8" stroke-width="1.5"/>
        <path d="M1 1l10 8 10-8" fill="none" stroke="#6cc5c8" stroke-width="1.5"/>
      </svg>
      marisolssilvercleaning@fernmail.test
    </p>
    <p class="contact-line contact-abn">
      <span class="abn-label">ABN :</span> 47193802564
    </p>
    <div class="accent-band"></div>
  </section>

</main>
</body>
</html>
```